Podcast Graphics For Internet Business Building Podcast

We need new podcast graphics.
1400x1400
300dpi

Needs to include text "Quiet Harbor Ledger Hour" as the podcast title and "Creative Internet Income Strategies" as a subtitle.

We like blue and grey as our main colors, but are open to other schemes.

Please see attached image for an example of podcast graphics we like. While we prefer a more plain look, it would be nice to have a subtle hint related to a "machine" in the background. Something like a pencil sketch of cogs like on the Quiet Harbor Ledger 10 book cover (attached image).

Target Market(s)

online entrepreneurs or those who want to start an online business

Font styles to use
Sans Serif

Colors
0455a3
3277b5

Requirements
Must have
• Text noted in project description
Should not have
• No money symbols or flashy "make money" type things.

```html
<!DOCTYPE html>
<html lang="en">
<head>
<meta charset="utf-8">
<title>Quiet Harbor Ledger Hour – Podcast Cover</title>
<link rel="stylesheet" href="https://fonts.googleapis.com/css2?family=Cinzel:wght@700&family=Oswald:wght@500&display=swap">
<style>
  :root {
    --page: #ffffff;
    --navy-deep: #0b1f56;
    --navy: #0a2a78;
    --royal: #0455a3;
    --royal-soft: #3277b5;
    --gold: #ffcc00;
    --white: #ffffff;
  }
  html, body {
    margin: 0;
    padding: 0;
    width: 1177px;
    height: 1200px;
    overflow: hidden;
    background: var(--page);
  }
  .canvas {
    position: relative;
    width: 1177px;
    height: 1200px;
  }
  .cover {
    position: absolute;
    left: 0;
    top: 0;
  }
  .title-line {
    font-family: "Cinzel", "Times New Roman", serif;
    font-weight: 700;
    font-size: 116px;
    letter-spacing: 2px;
    fill: var(--white);
  }
  .title-line--accent { fill: var(--gold); }
  .subtitle {
    font-family: "Oswald", "Arial Narrow", sans-serif;
    font-weight: 500;
    font-size: 46px;
    fill: var(--white);
  }
  .accent-bar { fill: var(--gold); }
  .rule { stroke: var(--gold); stroke-width: 3.5; }
</style>
</head>
<body>
<div class="canvas">
  <svg class="cover" width="1177" height="1200" viewBox="0 0 1177 1200" xmlns="http://www.w3.org/2000/svg">
    <defs>
      <linearGradient id="panelGradient" x1="1" y1="0" x2="0" y2="1">
        <stop offset="0" stop-color="var(--navy-deep)"/>
        <stop offset="0.45" stop-color="var(--navy)"/>
        <stop offset="1" stop-color="var(--royal)"/>
      </linearGradient>
      <radialGradient id="machineGlow" cx="0.3" cy="0.75" r="0.6">
        <stop offset="0" stop-color="var(--royal-soft)" stop-opacity="0.35"/>
        <stop offset="1" stop-color="var(--royal-soft)" stop-opacity="0"/>
      </radialGradient>
    </defs>

    <g class="cover-panel">
      <rect x="155" y="137" width="896" height="895" fill="url(#panelGradient)"/>
      <rect x="155" y="137" width="896" height="895" fill="url(#machineGlow)"
            role="img" aria-label="Faint background of interlocking machine cogs and a wireframe grid"/>
    </g>

    <rect class="accent-bar" x="278" y="137" width="649" height="28"/>
    <rect class="accent-bar" x="278" y="1004" width="649" height="28"/>

    <g class="podcast-title" text-anchor="middle">
      <text class="title-line" x="603" y="391">QUIET</text>
      <text class="title-line" x="603" y="512">HARBOR</text>
      <text class="title-line title-line--accent" x="603" y="634">LEDGER</text>
      <text class="title-line" x="603" y="755">HOUR</text>
    </g>

    <line class="rule" x1="270" y1="815" x2="935" y2="815"/>
    <text class="subtitle" x="280" y="866" textLength="645" lengthAdjust="spacingAndGlyphs">CREATIVE INTERNET INCOME STRATEGIES</text>
    <line class="rule" x1="270" y1="882" x2="935" y2="882"/>
  </svg>
</div>
</body>
</html>
```